Wedding invitation - including print files

Details
45 invitations and envelopes required

Our names: Corin and Marisol

Wedding information
Venue
At the Pennington residence, 2847 Thornbury-Waipiro road, Clevedon, Auckland for both the ceremony and reception.

Date
Saturday 19th April 2025 (Easter weekend)

Timing
Ceremony is at 3pm

Transport
A bus will pick up at 1.30pm from Linden Crest Hotel
A bus will go back to town to at 11pm and 12.15am to Linden Crest Hotel with a stop through Clevedon for those staying closer to the venue.

Accomodation
A lot of roomshares and hotels in clevedon if you wish to stay closer

Gifts
gifts aren’t necessary but a wishing well for a piece of art we will remember the day by.

Day After
We will be having some platters from 1pm on Sunday at (I will confirm this to you tomorrow sorry we are choosing between two places)

RSVP
By the 12th October 2024 to Corin 0279416652 corin@brantleygroup.co or Marisol 0278815927 marisol@quellastudio.co.nz

Here are concept ideas for the invitations and the aspects we like about them.
Three sided is practical to fit information

Font styles to use
Decorative

Colors

Designer to choose only greyscale colors for use in the design.

Requirements
Nice to have
• refer attachments and description
Should not have
• cant look cheap or tacky

```html
<!DOCTYPE html>
<html lang="en">
<head>
<meta charset="utf-8">
<title>Corin &amp; Marisol – Wedding Invitation</title>
<link rel="stylesheet" href="https://fonts.googleapis.com/css2?family=Great+Vibes&family=Open+Sans:ital,wght@0,400;0,600;0,700;1,400;1,700&display=swap">
<style>
  :root {
    --page: #e9e9ee;
    --card: #f8edf1;
    --ink: #111114;
    --ink-soft: #3f3f44;
    --navy: #373b6b;
    --navy-soft: #9a9cbc;
    --dots: #9a9aa2;
  }
  * { margin: 0; padding: 0; box-sizing: border-box; }
  html, body {
    width: 1068px; height: 1200px; overflow: hidden;
    background: var(--page);
    font-family: "Open Sans", Arial, sans-serif;
    color: var(--ink);
  }
  .invitation {
    position: absolute; left: 20px; top: 214px;
    width: 1028px; height: 772px;
    background: var(--card);
    box-shadow: 0 2px 10px rgba(0,0,0,.08);
    overflow: hidden;
  }
  .block { position: absolute; text-align: center; }
  .floral {
    position: absolute;
  }
  .floral--top-right {
    right: 0; top: 0; width: 300px; height: 220px;
    background: radial-gradient(ellipse at 75% 30%, var(--navy-soft) 0%, rgba(154,156,188,.55) 45%, rgba(248,237,241,0) 72%);
  }
  .floral--bottom-left {
    left: 0; bottom: 0; width: 600px; height: 300px;
    background: radial-gradient(ellipse at 40% 85%, var(--navy-soft) 0%, rgba(154,156,188,.55) 45%, rgba(248,237,241,0) 72%);
  }
  .day-after {
    left: 75px; top: 72px; width: 200px;
    text-align: left; font-size: 11.5px; line-height: 1.3;
    text-transform: uppercase; transform: rotate(3deg);
  }
  .rsvp { left: 40px; top: 220px; width: 240px; }
  .rsvp__title { font-weight: 700; font-style: italic; font-size: 22px; line-height: 1.1; }
  .rsvp__by { font-style: italic; font-size: 12.5px; color: var(--ink-soft); line-height: 1.3; }
  .rsvp__name { font-weight: 600; font-size: 13px; color: var(--ink-soft); margin-top: 8px; }
  .rsvp__phone { font-weight: 700; font-size: 17px; }
  .rsvp__email { font-weight: 600; font-size: 12px; color: var(--ink-soft); }
  .divider {
    height: 0; border-top: 2px dotted var(--dots);
    width: 150px; margin: 6px auto;
  }
  .centre { left: 385px; width: 240px; }
  .invite-line { top: 72px; font-weight: 700; font-size: 13px; line-height: 1.35; text-transform: uppercase; }
  .couple {
    top: 180px; font-family: "Great Vibes", cursive;
    color: var(--navy); font-size: 56px; line-height: .95;
  }
  .details { top: 405px; }
  .details__title { font-weight: 700; font-style: italic; font-size: 25px; line-height: 1.1; }
  .details__text { font-weight: 600; font-size: 14px; color: var(--ink-soft); line-height: 1.2; }
  .info { left: 680px; width: 320px; }
  .info__title { font-weight: 700; font-size: 20px; line-height: 1.2; }
  .info__text { font-size: 9.5px; line-height: 1.35; text-transform: uppercase; }
  .info__text--venue { text-transform: none; color: var(--ink-soft); font-size: 10px; }
  .venue { top: 240px; }
  .transport { top: 356px; }
  .accommodation { top: 508px; }
  .gifts { top: 622px; }
</style>
</head>
<body>
  <main class="invitation">
    <div class="floral floral--top-right" role="img" aria-label="Navy line-drawn roses and blossom sprigs in the top right corner"></div>
    <div class="floral floral--bottom-left" role="img" aria-label="Navy line-drawn roses, leaves and blossom sprigs along the bottom left"></div>

    <p class="block day-after">Day after we will be having some platters from 1pm on Sunday at (I will confirm this to you tomorrow sorry we are choosing between two places)</p>

    <section class="block rsvp">
      <h2 class="rsvp__title">RSVP</h2>
      <p class="rsvp__by">By the<br>12th October 2024<br>to</p>
      <p class="rsvp__name">Corin <span class="rsvp__phone">0279416652</span></p>
      <p class="rsvp__email">corin@brantleygroup.co</p>
      <div class="divider"></div>
      <p class="rsvp__name" style="margin-top:0">or Marisol <span class="rsvp__phone">0278815927</span></p>
      <p class="rsvp__email">marisol@quellastudio.co.nz</p>
    </section>

    <p class="block centre invite-line">Join us for our<br>wedding</p>
    <h1 class="block centre couple">Corin<br>&amp;<br>Marisol</h1>

    <section class="block centre details">
      <h2 class="details__title">DATE</h2>
      <p class="details__text">Saturday 19th April 2025<br>(Easter weekend)</p>
      <div class="divider" style="width:160px;margin:10px auto 8px"></div>
      <h2 class="details__title">TIMING</h2>
      <p class="details__text">Ceremony is at 3pm</p>
    </section>

    <section class="block info venue">
      <h2 class="info__title">VENUE</h2>
      <p class="info__text info__text--venue">At the Pennington residence, 2847<br>Thornbury-Waipiro road, Clevedon, Auckland<br>for both the ceremony and reception.</p>
      <div class="divider" style="margin-top:22px"></div>
    </section>

    <section class="block info transport">
      <h2 class="info__title">TRANSPORT</h2>
      <p class="info__text" style="margin-top:8px">A bus will pick up at 1.30pm from Linden Crest Hotel</p>
      <p class="info__text" style="margin-top:8px">A bus will go back to town to at 11pm and 12.15am<br>to Linden Crest Hotel with a stop through Clevedon<br>for those staying closer to the venue.</p>
      <div class="divider" style="margin-top:22px"></div>
    </section>

    <section class="block info accommodation">
      <h2 class="info__title">ACCOMODATION</h2>
      <p class="info__text" style="margin-top:6px">A lot of roomshares and hotels in<br>Clevedon if you wish to stay closer</p>
      <div class="divider" style="margin-top:18px"></div>
    </section>

    <section class="block info gifts">
      <h2 class="info__title">GIFTS</h2>
      <p class="info__text">Gifts aren’t necessary but a<br>wishing well for a piece of art we<br>will remember the day by</p>
    </section>
  </main>
</body>
</html>
```